Buff Works Business card design

i need a business card design for my new detailing company called 'Brent's Detail Shop'. i want an all black and white design . simple, direct and to the point. i want the designer to choose a fitting font to match the logothe front should have logo, address, phone and email and the back side should have a slogan and text indicating that we offer services on anything including cars, trucks, motorcycles and RVs. slogan will read "we take pride in your ride"
maybe also very small on the back side the IG icon with Brents_Detail_Shop

phone 208.474.2863
address 3847 E Larkmoor Ave
Spokane WA 98734
email: BrentsDetail@quorvamail.com

Target Market(s)

all ages , auto enthusiasts

Industry/Entity Type

Automotive

Contact Information for Business Card

the front should have logo, address, phone and email and the back side should have a slogan and text indicating that we offer services on anything including cars, trucks, motorcycles and RVs. slogan will read "we take pride in your ride"

phone 208.474.2863
address 3847 E Larkmoor Ave
Spokane WA 98734

Colors
000000
ffffff

Requirements
Must have
• bold font and very simple design with good spacing
Nice to have
• anything creative from the designer indicating we service any types of vehicles
Should not have
• any colors ,

```html
<!DOCTYPE html>
<html lang="en">
<head>
<meta charset="utf-8">
<title>Brent's Detail Shop – Business Card</title>
<link href="https://fonts.googleapis.com/css2?family=Arvo:wght@400;700&family=Roboto+Slab:wght@300;700&display=swap" rel="stylesheet">
<style>
  :root {
    --stage: #3b3b3b;
    --paper: #ffffff;
    --ink: #000000;
    --card-dark: #141414;
    --ghost: #222222;
  }
  * { box-sizing: border-box; margin: 0; padding: 0; }
  html, body { width: 1200px; height: 1000px; overflow: hidden; }
  body {
    background: var(--stage);
    font-family: "Arvo", "Roboto Slab", serif;
    position: relative;
  }
  .card {
    position: absolute;
    left: 220px;
    width: 760px;
    height: 434px;
    border-radius: 28px;
    overflow: hidden;
  }
  .card--front { top: 52px; background: var(--paper); color: var(--ink); }
  .card--back  { top: 514px; background: var(--card-dark); color: var(--paper); }

  /* Front */
  .brand-mark {
    position: absolute;
    left: 120px; top: 127px;
    width: 200px;
    display: flex; flex-direction: column; align-items: center; gap: 12px;
  }
  .brand-mark__circle {
    width: 70px; height: 70px; border-radius: 50%;
    background: var(--ink);
  }
  .brand-mark__name {
    font-family: "Arvo", serif; font-weight: 700;
    font-size: 22px; line-height: 1.15; text-align: center;
  }
  .divider {
    position: absolute; left: 362px; top: 150px;
    width: 2px; height: 118px; background: var(--ink);
  }
  .contact {
    position: absolute; left: 386px; top: 150px;
    list-style: none;
    font-family: "Arvo", serif; font-weight: 700;
    font-size: 17px; line-height: 1.2;
  }
  .contact__item { display: flex; align-items: flex-start; gap: 8px; margin-bottom: 8px; }
  .contact__icon { width: 13px; height: 15px; flex: none; margin-top: 2px; }

  /* Back */
  .ghost-mark {
    position: absolute; left: 200px; top: 40px;
    width: 340px; height: 340px; border-radius: 50%;
    border: 16px solid var(--ghost);
    display: flex; align-items: center; justify-content: center;
    color: var(--ghost);
    font-family: "Arvo", serif; font-weight: 700; font-size: 44px;
    text-align: center; line-height: 1.1;
  }
  .slogan {
    position: absolute; left: 0; right: 0; top: 168px;
    text-align: center;
    font-family: "Arvo", serif; font-weight: 700;
    font-size: 33px; letter-spacing: 0.5px; text-transform: uppercase;
  }
  .services {
    position: absolute; left: 0; right: 0; top: 268px; text-align: center;
  }
  .services__label {
    font-family: "Roboto Slab", serif; font-weight: 300;
    font-size: 16px; text-transform: uppercase; letter-spacing: 0.5px;
  }
  .services__list {
    margin-top: 10px;
    font-family: "Arvo", serif; font-weight: 700;
    font-size: 19px; text-transform: uppercase; letter-spacing: 0.5px;
  }
  .social {
    position: absolute; right: 36px; bottom: 30px;
    display: flex; align-items: center; gap: 8px;
    font-family: "Arvo", serif; font-weight: 700; font-size: 13px;
  }
  .social__square { width: 14px; height: 14px; border: 2px solid var(--paper); border-radius: 3px; }
</style>
</head>
<body>

<section class="card card--front" aria-label="Card front">
  <div class="brand-mark">
    <span class="brand-mark__circle"></span>
    <span class="brand-mark__name">Brent's<br>Detail Shop</span>
  </div>
  <span class="divider"></span>
  <ul class="contact">
    <li class="contact__item">
      <svg class="contact__icon" viewBox="0 0 12 16" aria-hidden="true"><path d="M6 0C2.7 0 0 2.6 0 5.9 0 10.3 6 16 6 16s6-5.7 6-10.1C12 2.6 9.3 0 6 0zm0 8.3A2.4 2.4 0 1 1 6 3.5a2.4 2.4 0 0 1 0 4.8z" fill="currentColor"/></svg>
      <span>3847 E Larkmoor Ave<br>Spokane WA 98734</span>
    </li>
    <li class="contact__item">
      <svg class="contact__icon" viewBox="0 0 16 16" aria-hidden="true"><path d="M3.6 1l2.3 3.2-1.4 1.6c.9 2 2.6 3.7 4.6 4.6l1.6-1.4L14 11.3 12.6 14C6.5 13.7 2.3 9.5 2 3.4z" fill="currentColor"/></svg>
      <span>208.474.2863</span>
    </li>
    <li class="contact__item">
      <svg class="contact__icon" viewBox="0 0 16 12" aria-hidden="true"><rect x="1" y="1" width="14" height="10" rx="1" fill="none" stroke="currentColor" stroke-width="2"/><path d="M1 1l7 6 7-6" fill="none" stroke="currentColor" stroke-width="2"/></svg>
      <span>BrentsDetail@quorvamail.com</span>
    </li>
  </ul>
</section>

<section class="card card--back" aria-label="Card back">
  <div class="ghost-mark">Brent's<br>Detail Shop</div>
  <h1 class="slogan">We take pride in your ride</h1>
  <div class="services">
    <p class="services__label">Services offered on:</p>
    <p class="services__list">Cars &bull; Trucks &bull; Motorcycles &bull; RVs</p>
  </div>
  <div class="social">
    <span class="social__square"></span>
    <span>Pictogrid</span>
  </div>
</section>

</body>
</html>
```